Lumen Harbor Sales Aid and Contract

I started my own company and the company I worked for has a sales aid / contract that I want to replicate. I want it to be simpler similar design in an editable PDF Form. It needs to be different and better in my company colors see logo attached I need to be able to edit the fine print and will need the KP Inc. changed to Lumen Harbor through out the agreement. Follow same flow but instead of Platinum Gold and Silver I would like Gold Silver and Bronze with different badges

```html
<!DOCTYPE html>
<html lang="en">
<head>
<meta charset="utf-8">
<title>Lumen Harbor Sales Aid and Contract</title>
<link href="https://fonts.googleapis.com/css2?family=Montserrat:wght@800&family=Open+Sans:ital,wght@0,400;0,700;1,400&family=Roboto:wght@400&family=Tinos&display=swap" rel="stylesheet">
<style>
:root{
  --board:#e8e8e8;
  --ink:#333333;
  --paper:#ffffff;
  --field:#e4e6f3;
  --line:#b9b9b9;
  --grid:#d6d6d6;
  --text:#2a2a2a;
  --muted:#8a8a8a;
  --gold-light:#f6d24a;
  --gold:#d99a12;
  --silver-light:#cdd8e2;
  --silver:#7f93a8;
  --bronze-light:#f0a05a;
  --bronze:#b85a1c;
  --seal-dark:#2a2a2a;
  --seal-gold:#b88f2a;
}
*{box-sizing:border-box;margin:0;padding:0}
html,body{width:1200px;height:1136px;overflow:hidden;background:var(--board)}
body{position:relative;font-family:"Open Sans",Arial,sans-serif;color:var(--text)}
.intro{position:absolute;left:64px;top:478px;font-family:"Roboto",Arial,sans-serif;font-size:42px;line-height:62.5px;color:#111}
.page{position:absolute;width:365px;height:277px;background:var(--ink);box-shadow:0 1px 3px rgba(0,0,0,.25)}
.sheet{position:absolute;left:0;background:var(--paper)}
.brand{position:absolute;left:12px;top:8px;display:flex;align-items:center}
.brand-dot{width:22px;height:22px;border:2px solid #fff;border-radius:50%}
.title{position:absolute;font-family:"Montserrat",Arial,sans-serif;font-weight:800;font-size:16px;color:#fff;transform:translateX(-50%);white-space:nowrap}
.tiny{position:absolute;font-size:4.4px;line-height:1.2;white-space:nowrap}
.field{position:absolute;background:var(--field)}
.row{position:absolute;left:12px;width:102px;height:8px;border:0.5px solid var(--line);font-size:4.4px;line-height:7px;padding-left:2px}
.row .field{left:28px;top:1px;right:1px;height:5.5px}
.q{position:absolute;left:14px;font-size:4.4px;white-space:nowrap}
.grid{position:absolute;border:0.6px dashed var(--grid);
  background-image:linear-gradient(to right,transparent calc(100% - 0.5px),var(--grid) 0),linear-gradient(to bottom,transparent calc(100% - 0.5px),var(--grid) 0);
  background-size:10% 10%}
.grid-label{position:absolute;font-family:"Tinos",serif;font-size:5px;color:#777;text-decoration:underline;transform:translateX(-50%)}
.option{position:absolute;top:35px;width:107px;height:221px;border:0.6px solid #aaa;background:#fff}
.option .caption{position:absolute;top:26px;width:100%;text-align:center;font-size:4.6px;font-weight:700}
.option .field{left:5px;top:39px;width:96px;height:163px}
.option .total{position:absolute;left:8px;top:214px;font-size:4.4px;font-weight:700}
.option .total span{display:inline-block;width:44px;border-bottom:0.5px solid #555;margin-left:2px}
.badge-art{position:absolute;left:50%;top:-8px;width:40px;height:32px;transform:translateX(-50%);border-radius:3px}
.badge-gold{background:linear-gradient(180deg,var(--gold-light),var(--gold))}
.badge-silver{background:linear-gradient(180deg,var(--silver-light),var(--silver))}
.badge-bronze{background:linear-gradient(180deg,var(--bronze-light),var(--bronze))}
.seal-art{position:absolute;left:8px;top:8px;width:34px;height:34px;border-radius:3px;background:linear-gradient(135deg,var(--seal-gold),var(--seal-dark))}
.budget-box{position:absolute;top:131px;width:61px;height:30px;border:0.6px solid #999;border-radius:4px;background:#fff}
.budget-box .field{left:3px;top:8px;right:3px;height:13px}
.fine{position:absolute;left:14px;width:320px;font-family:Arial,sans-serif;font-size:3.9px;line-height:1.3}
.fine b{font-weight:700}
.form-line{position:absolute;font-family:Arial,sans-serif;font-size:4.2px;white-space:nowrap}
.u{display:inline-block;border-bottom:0.5px solid #555;vertical-align:bottom}
</style>
</head>
<body>

<p class="intro">Some pages<br>of the agreement<br>Others pages will<br>come if<br>I selected</p>

<section class="page" style="left:31px;top:87px">
  <div class="brand"><span class="brand-dot"></span></div>
  <h2 class="title" style="left:182px;top:12px">Discovery</h2>
  <div class="sheet" style="top:38px;width:348px;height:230px">
    <div class="tiny" style="left:12px;top:4px;width:332px;height:8px;border:0.5px solid var(--line);padding:1px 2px">
      Incoming call : Date: <span class="u" style="width:30px"></span>Owner of property: (YES) (NO)&nbsp; Date of appointment: <span class="u" style="width:30px"></span>
      <span style="position:absolute;right:8px;top:1.5px;font-size:3.5px">Exterior - Interior - Masonry - Concrete - Home</span>
    </div>
    <div class="row" style="top:14px">Name:<span class="field"></span></div>
    <div class="row" style="top:24px">Address:<span class="field"></span></div>
    <div class="row" style="top:34px">City:<span class="field"></span></div>
    <div class="row" style="top:44px">Best contact number:<span class="field" style="left:50px"></span></div>
    <div class="row" style="top:54px">Best e-mail:<span class="field"></span></div>
    <div class="row" style="top:65px">Other Decision Makers:<span class="field" style="left:50px"></span></div>
    <div class="row" style="top:76px">Contact Number:<span class="field" style="left:38px"></span></div>
    <div class="tiny" style="left:13px;top:88px;font-style:italic;color:var(--muted)">After initial introduction&nbsp; on location</div>
    <div style="position:absolute;left:116px;top:13px;width:226px;height:91px;border:0.6px solid var(--line)">
      <div class="tiny" style="left:2px;top:1px">Tell me a little about your project:</div>
      <span class="field" style="left:2px;top:8px;right:2px;bottom:2px"></span>
    </div>
    <p class="q" style="top:108px">1.&nbsp;&nbsp; Would it be ok if we discuss some of the details regarding your project? &nbsp;.... this will help insure we get the results your looking for!</p>
    <p class="q" style="top:119px">2.&nbsp;&nbsp; Do you have any sketches or drawings? If yes, would you mind sharing them with me?&nbsp; If no, that's ok we will cover that today!</p>
    <p class="q" style="top:131px">3.&nbsp;&nbsp; Is there anything else you don't like about your existing ( <span class="field" style="position:relative;display:inline-block;width:180px;height:5px"></span> )?</p>
    <p class="q" style="top:143px">4.&nbsp;&nbsp; Have you ever done a construction project?&nbsp; Y / N <span class="field" style="position:relative;display:inline-block;width:200px;height:5px"></span></p>
    <p class="q" style="top:154px">5.&nbsp;&nbsp; What's the biggest thing your hoping to achieve by doing ( <span class="field" style="position:relative;display:inline-block;width:35px;height:5px"></span> )? <span class="field" style="position:relative;display:inline-block;width:143px;height:5px"></span></p>
    <p class="q" style="top:166px">6.&nbsp;&nbsp; Do you have any questions or concerns about any other portion of your property or home <span class="field" style="position:relative;display:inline-block;width:110px;height:5px"></span> ?</p>
    <p class="q" style="top:178px">7.&nbsp;&nbsp; Hypothetically if you were to move forward, how do you envision this project to go as far as time lines and completions dates?</p>
    <p class="q" style="left:19px;top:192px">Start date &nbsp;<span class="u" style="width:268px;border-bottom-style:dashed;margin-bottom:2px"></span> Finish date</p>
    <p class="tiny" style="left:156px;top:197px">TIME LINE DATE</p>
    <p class="q" style="top:208px">8.&nbsp;&nbsp; Service Type: <span class="field" style="position:relative;display:inline-block;width:76px;height:5px"></span> Project Manager: <span class="field" style="position:relative;display:inline-block;width:76px;height:5px"></span> Crew: <span class="field" style="position:relative;display:inline-block;width:76px;height:5px"></span></p>
    <p class="q" style="top:220px">9.&nbsp;&nbsp; Safety Concerns: <span class="field" style="position:relative;display:inline-block;width:276px;height:5px"></span></p>
  </div>
</section>

<section class="page" style="left:418px;top:87px">
  <div class="brand"><span class="brand-dot"></span></div>
  <h2 class="title" style="left:272px;top:12px">Notes</h2>
  <div class="sheet" style="top:40px;width:343px;height:210px">
    <div style="position:absolute;left:14px;top:5px;width:322px;height:199px;border:0.6px solid var(--line)">
      <div class="tiny" style="left:3px;top:2px;color:var(--muted)">Tell me a little about your project:</div>
      <span class="field" style="left:2px;top:9px;right:2px;bottom:2px"></span>
    </div>
  </div>
</section>

<section class="page" style="left:804px;top:87px">
  <div class="brand"><span class="brand-dot"></span></div>
  <div class="sheet" style="top:60px;width:344px;height:190px">
    <div class="grid-label" style="left:177px;top:1px">Sketch and Design</div>
    <div class="grid" style="left:14px;top:14px;width:319px;height:168px"></div>
  </div>
</section>

<section class="page" style="left:418px;top:379px">
  <div class="brand"><span class="brand-dot"></span></div>
  <h2 class="title" style="left:181px;top:12px">Discovery</h2>
  <div class="sheet" style="top:40px;width:343px;height:210px">
    <p class="tiny" style="left:14px;top:8px">12 – Like with any project… making sure the budget numbers are real and there are no surprises later… is pretty important. Wouldn't you agree?</p>
    <p class="tiny" style="left:14px;top:19px">What our clients have found, is this little step to be very valuable and it really points us in the right direction.</p>
    <p class="tiny" style="left:176px;top:40px;transform:translateX(-50%);font-size:5px;font-weight:700;text-decoration:underline">We can take most&nbsp; projects and&nbsp; break them into three categories or budget areas</p>
  </div>
  <div class="budget-box" style="left:61px"><span class="field"></span></div>
  <div class="budget-box" style="left:153px"><span class="field"></span></div>
  <div class="budget-box" style="left:248px"><span class="field"></span></div>
  <p class="tiny" style="left:14px;top:222px">13 -&nbsp; Taking a look at each box, which category do you believe fits your budget?&nbsp; This is just a plumb line as to which direction we move to next!</p>
</section>

<section class="page" style="left:804px;top:379px">
  <div class="sheet" style="top:27px;width:344px;height:233px"></div>
  <h2 class="title" style="left:82px;top:4px">Options</h2>
  <div class="option" style="left:12px">
    <div class="badge-art badge-gold" role="img" aria-label="Gold guarantee badge artwork"></div>
    <p class="caption">10 Year Workmanship Guarantee</p>
    <span class="field"></span>
    <p class="total">Investment Total<span></span></p>
  </div>
  <div class="option" style="left:124px">
    <div class="badge-art badge-silver" role="img" aria-label="Silver guarantee badge artwork"></div>
    <p class="caption">5 Year Workmanship Guarantee</p>
    <span class="field"></span>
    <p class="total">Investment Total<span></span></p>
  </div>
  <div class="option" style="left:235px">
    <div class="badge-art badge-bronze" role="img" aria-label="Bronze guarantee badge artwork"></div>
    <p class="caption">2 Year Workmanship Guarantee</p>
    <span class="field"></span>
    <p class="total">Investment Total<span></span></p>
  </div>
  <div class="seal-art" role="img" aria-label="Guarantee seal artwork"></div>
</section>

<section class="page" style="left:418px;top:672px">
  <div class="brand"><span class="brand-dot"></span></div>
  <h2 class="title" style="left:181px;top:26px">Design</h2>
  <div class="sheet" style="top:59px;width:343px;height:191px">
    <div class="grid-label" style="left:176px;top:1px">Sketch and Design</div>
    <div class="grid" style="left:13px;top:15px;width:319px;height:167px"></div>
  </div>
</section>

<section class="page" style="left:804px;top:672px">
  <div class="brand"><span class="brand-dot"></span></div>
  <h2 class="title" style="left:183px;top:22px">Agreement</h2>
  <div class="sheet" style="top:59px;width:344px;height:194px">
    <p class="fine" style="top:4px"><b>Terms:</b><br>Your guarantee (based on your choice) is on workmanship and not materials, which would be covered under the manufacturer's warranty. This workmanship guarantee is non transferable.</p>
    <p class="fine" style="top:24px"><b>Qualification:</b> Your investment of the Gold / Silver / Bronze system must be paid in full. During the terms of the workmanship guarantee, if defects in workmanship are found, original home owner must notify Lumen Harbor Inc. within 10 days by telephone or e-mail and confirm by written notice. Limitations: guarantee does not cover acts of omissions of other trades, natural weathering, recommended maintenance, lightning, flood, earthquake or any natural disaster or unusual phenomenon of elements.</p>
    <p class="fine" style="top:51px"><b>PRE-LIEN NOTICE</b> to (Owners Authorized Agents) by Contractor: "Any person or company supplying labor or materials for this improvement to your property may file a lien against your property if that person or company is not paid for contributions. Authorization: I have authorized work task to be completed. I agree that seller retains title to equipment or product and materials furnished until final payment is satisfied.</p>
    <p class="form-line" style="left:14px;top:77px">Date: <span class="field" style="position:relative;display:inline-block;width:40px;height:6px"></span> Level plan : <span class="u" style="width:58px"></span> Start date: <span class="field" style="position:relative;display:inline-block;width:50px;height:6px"></span> Planned completion date: <span class="field" style="position:relative;display:inline-block;width:40px;height:6px"></span></p>
    <p class="form-line" style="left:14px;top:89px">Client's Name: <span class="field" style="position:relative;display:inline-block;width:92px;height:6px"></span> Project Location address: <span class="field" style="position:relative;display:inline-block;width:140px;height:6px"></span></p>
    <p class="form-line" style="left:14px;top:104px">Total Investment: <span class="field" style="position:relative;display:inline-block;width:118px;height:6px"></span> Payment terms: <span class="field" style="position:relative;display:inline-block;width:129px;height:6px"></span></p>
    <p class="form-line" style="left:14px;top:116px">Amount down: <span class="field" style="position:relative;display:inline-block;width:124px;height:6px"></span> Payment method: <span class="field" style="position:relative;display:inline-block;width:66px;height:6px"></span> Date: <span class="field" style="position:relative;display:inline-block;width:42px;height:6px"></span></p>
    <p class="form-line" style="left:14px;top:129px">Clients authorization: <span class="u" style="width:106px"></span> Printed name <span class="field" style="position:relative;display:inline-block;width:136px;height:6px"></span></p>
    <p class="form-line" style="left:14px;top:141px">Special instructions:</p>
    <span class="field" style="left:61px;top:144px;width:279px;height:29px"></span>
    <p class="form-line" style="left:12px;top:181px"><span style="font-size:3px;font-weight:700">Lumen Harbor Inc.</span>&nbsp; By <span class="u" style="width:84px"></span>&nbsp;&nbsp; Title <span class="field" style="position:relative;display:inline-block;width:60px;height:6px"></span> Date: <span class="field" style="position:relative;display:inline-block;width:58px;height:6px"></span></p>
  </div>
  <p class="tiny" style="left:183px;top:259px;transform:translateX(-50%);font-family:Arial,sans-serif;font-size:3.6px;color:#fff">A Copy will be made available to client within 24 hours&nbsp; of agreement authorization</p>
</section>

</body>
</html>
```